Tembo & Lusani Advocates website

An interactive professional law firm website fully synchronized with social media pages.

Target Market(s)

Corporations and professionals

Industry/Entity Type

Professional Service

Number of Pages Required

5+ page

Font styles to use
Sans Serif

Colors

Designer to choose colors to be used in the design.

```html
<!DOCTYPE html>
<html lang="en">
<head>
<meta charset="utf-8">
<title>Tembo &amp; Lusani Advocates</title>
<link href="https://fonts.googleapis.com/css2?family=Lato:wght@300;400;700;900&family=Marcellus&display=swap" rel="stylesheet">
<style>
:root{
  --red:#8c1b20;
  --ink:#2b2b2b;
  --muted:#555;
  --line:#cfcfcf;
  --grey-bg:#ebeaea;
  --footer:#1d1d1d;
  --white:#fff;
}
*{margin:0;padding:0;box-sizing:border-box}
html,body{width:1200px;height:4138px;overflow:hidden}
body{font-family:'Lato',sans-serif;color:var(--ink);background:var(--white);position:relative}

/* header */
.site-header{position:absolute;top:0;left:0;width:1200px;height:152px;background:var(--white)}
.brand{position:absolute;left:88px;top:40px;display:flex;align-items:center;gap:12px}
.brand-square{width:26px;height:26px;background:var(--red)}
.brand-name{font-family:'Lato',sans-serif;font-weight:700;font-size:22px;color:var(--ink)}
.brand-tag{position:absolute;left:88px;top:96px;font-size:8px;letter-spacing:2px;color:#999;text-transform:uppercase}
.header-phone{position:absolute;left:770px;top:38px;display:flex;align-items:center;gap:10px;font-size:21px;font-weight:700;color:var(--ink)}
.icon-circle{width:26px;height:26px;border-radius:50%;background:var(--red);display:flex;align-items:center;justify-content:center}
.socials{display:flex;gap:5px}
.socials span{width:20px;height:20px;border-radius:50%;background:var(--red);display:block}
.header-socials{position:absolute;left:1003px;top:41px}
.main-nav{position:absolute;left:556px;top:88px;display:flex;font-size:14px;font-weight:700}
.main-nav a{color:var(--ink);text-decoration:none;padding:0 20px;border-right:1px solid #bbb}
.main-nav a:last-child{border-right:0;padding-right:0}
.main-nav a.active{color:var(--red)}

/* hero */
.hero{position:absolute;top:152px;left:0;width:1200px;height:668px;background:linear-gradient(180deg,#5d6468 0%,#7b8286 40%,#4c5256 100%)}
.hero-title{position:absolute;top:245px;width:100%;text-align:center;font-family:'Marcellus',serif;font-weight:400;color:var(--white);font-size:78px;line-height:82px}
.hero-text{position:absolute;top:440px;left:200px;width:800px;text-align:center;color:var(--white);font-size:14px;line-height:22px}
.hero-btn{position:absolute;top:522px;left:520px;width:160px;height:42px;border:2px solid var(--white);color:var(--white);font-weight:700;font-size:14px;display:flex;align-items:center;justify-content:center}
.hero-arrow{position:absolute;top:300px}

/* section titles */
.section-title{position:absolute;font-size:30px;font-weight:700;color:var(--ink)}
.section-title em{font-style:normal;color:var(--red)}
.rule{position:absolute;height:1px;background:var(--line)}
.btn-outline{position:absolute;width:148px;height:42px;border:2px solid var(--red);color:var(--ink);font-weight:700;font-size:14px;display:flex;align-items:center;justify-content:center;background:var(--white)}

/* about */
.about-photo{position:absolute;left:91px;top:971px;width:331px;height:221px;background:linear-gradient(135deg,#3c3b3e,#6a5b55 60%,#2a2a2e)}
.about-text{position:absolute;font-size:13.5px;line-height:21px;color:var(--muted);text-align:justify}

/* practice */
.practice{position:absolute;top:1410px;left:0;width:1200px;height:838px}
.practice-panel{position:absolute;left:0;top:0;width:601px;height:838px;background:var(--red)}
.practice-photo{position:absolute;left:601px;top:0;width:599px;height:838px;background:linear-gradient(160deg,#2e3d4d 0%,#6d7f90 45%,#a9b6c1 70%,#3b4a58 100%)}
.practice-title{position:absolute;left:88px;top:64px;font-size:28px;font-weight:700;color:var(--white)}
.practice-rule{position:absolute;left:88px;top:110px;width:486px;height:1px;background:rgba(255,255,255,.6)}
.practice-item{position:absolute;left:88px;width:486px;color:var(--white)}
.practice-item h3{font-size:20px;font-weight:700;margin-bottom:8px}
.practice-item p{font-size:13.5px;line-height:21px;text-align:justify}
.more-mark{display:inline-block;float:right;margin-top:4px;width:32px;height:12px;border:1px solid #fff}
.btn-light{position:absolute;left:88px;top:720px;width:148px;height:42px;border:2px solid var(--white);background:var(--white);color:var(--red);font-weight:700;font-size:14px;display:flex;align-items:center;justify-content:center}

/* professionals */
.professionals{position:absolute;top:2248px;left:0;width:1200px;height:820px;background:var(--grey-bg)}
.team-card{position:absolute;top:185px;width:284px;height:536px}
.team-photo{width:284px;height:290px;background:linear-gradient(180deg,#3a3a3a,#5a4a44 55%,#2b2b30)}
.team-body{width:284px;height:246px;background:var(--red);color:var(--white);padding:22px 26px;position:relative}
.team-body h4{font-size:15px;font-weight:900;letter-spacing:.3px}
.team-body .role{font-size:12px;margin-bottom:12px}
.team-body p{font-size:12px;line-height:18px}
.team-body .go{position:absolute;right:20px;bottom:14px}
.carousel-arrow{position:absolute;top:400px}

/* clients */
.client-row{position:absolute;left:91px;top:3264px;display:flex;gap:9px}
.client{width:144px;height:124px;background:#e6e6e6;display:flex;align-items:center;justify-content:center}
.client span{width:108px;height:92px;background:var(--white);border-radius:12px;display:flex;align-items:center;justify-content:center;font-size:13px;font-weight:700;color:#444;text-align:center}

/* footer */
.site-footer{position:absolute;top:3551px;left:0;width:1200px;height:587px;background:var(--footer);color:var(--white)}
.footer-column-photo{position:absolute;right:0;top:0;width:560px;height:587px;background:linear-gradient(90deg,var(--footer) 0%,#3a3a3a 45%,#5c5c5c 75%,#2a2a2a 100%)}
.footer-brand{position:absolute;left:136px;top:66px;display:flex;align-items:center;gap:12px;font-size:20px;font-weight:700;color:var(--white)}
.footer-brand i{width:24px;height:24px;background:var(--red);display:block}
.footer-heading{position:absolute;font-size:17px;font-weight:900;letter-spacing:.5px}
.footer-rule{position:absolute;height:1px;background:#555}
.quick-links{position:absolute;left:136px;top:197px;list-style:none;font-size:14px;font-weight:700;line-height:26px}
.quick-links li::before{content:"‹ ";color:#bbb}
.contact-block{position:absolute;left:397px;top:197px;font-size:12.5px;line-height:17px;color:#ddd}
.contact-line{display:flex;align-items:center;gap:8px}
.contact-line i{width:9px;height:9px;background:#ddd;border-radius:50%;display:inline-block}
.footer-phone{position:absolute;left:397px;top:452px;font-size:24px;font-weight:900}
.footer-socials{position:absolute;left:136px;top:452px}
.footer-socials span{background:var(--white);width:22px;height:22px}
.copyright{position:absolute;left:136px;top:524px;font-size:13px;color:#bbb}
</style>
</head>
<body>

<header class="site-header">
  <div class="brand"><span class="brand-square"></span><span class="brand-name">Tembo &amp; Lusani Advocates</span></div>
  <div class="brand-tag">Construction law | Arbitration | Litigation</div>
  <div class="header-phone">
    <span class="icon-circle"><svg width="14" height="14" viewBox="0 0 24 24"><path fill="#fff" d="M6.6 10.8a15 15 0 0 0 6.6 6.6l2.2-2.2a1 1 0 0 1 1-.25 11.4 11.4 0 0 0 3.6.6 1 1 0 0 1 1 1V20a1 1 0 0 1-1 1A17 17 0 0 1 3 4a1 1 0 0 1 1-1h3.5a1 1 0 0 1 1 1c0 1.25.2 2.45.6 3.6a1 1 0 0 1-.25 1z"/></svg></span>
    0414 555 210
  </div>
  <div class="socials header-socials"><span></span><span></span><span></span><span></span><span></span></div>
  <nav class="main-nav">
    <a class="active">About Us</a><a>Practice Areas</a><a>Our clients</a><a>Our Professionals</a><a>Contact Us</a>
  </nav>
</header>

<section class="hero" role="img" aria-label="Aerial photograph of city highway interchanges">
  <svg class="hero-arrow" style="left:58px" width="24" height="40" viewBox="0 0 24 40"><path d="M20 4 4 20l16 16" stroke="#fff" stroke-width="3" fill="none"/></svg>
  <svg class="hero-arrow" style="right:58px" width="24" height="40" viewBox="0 0 24 40"><path d="M4 4l16 16L4 36" stroke="#fff" stroke-width="3" fill="none"/></svg>
  <h1 class="hero-title">Tembo &amp; Lusani<br>Advocates</h1>
  <p class="hero-text">Lorem ipsum dolor sit amet, consectetur adipiscing elit. Quid autem habent admirationis, cum prope accesseris? An hoc usque quaque, aliter in vita? Non igitur de improbo, sed de callido improbo quaerimus, qualis Q.</p>
  <div class="hero-btn">READ MORE</div>
</section>

<h2 class="section-title" style="left:91px;top:896px"><em>About</em> Us</h2>
<div class="rule" style="left:91px;top:946px;width:1062px"></div>
<div class="about-photo" role="img" aria-label="Group photograph of the firm's partners and associates"></div>
<p class="about-text" style="left:441px;top:964px;width:712px">In 1996, our firm was founded and is comprised of 5 Partners and over 15 Associates and support staff fully engaged and focused on client service. The firm is fully automated and is run on the latest practice management software with efficient client focused delivery systems and improved turn around times.</p>
<p class="about-text" style="left:441px;top:1083px;width:712px">Over the years, the firm has worked with the International firm of Hartley Crane in succes fully representing Civic Rights Alliance against a multimillion dollar law suit and has acted for both local and international corporations from China, Italy, Turkey, South Africa, Zambia and the United Kingdom to build their businesses.</p>
<p class="about-text" style="left:91px;top:1201px;width:1062px">Tembo &amp; Lusani Advocates are a specialist commercial law firm in Uganda focusing on commercial litigation, construction law and arbitration. We have excelled in our niche areas for over two decades Vision And Mission and We have do it three Processes Integrity, Partnership and then Efficiency.</p>
<div class="btn-outline" style="left:91px;top:1288px">Read More</div>

<section class="practice">
  <div class="practice-panel"></div>
  <div class="practice-photo" role="img" aria-label="Photograph of a curving elevated highway seen from below"></div>
  <h2 class="practice-title">Practice Areas</h2>
  <div class="practice-rule"></div>
  <div class="practice-item" style="top:140px">
    <h3>Construction Law</h3>
    <p>Our Construction Law department is headed by our Senior Partner Daniel Lusani, who is highly qualified and experienced in Construction law and in providing advice on contract management under the Harbor, Keystone, Arden and Corva forms of contracts. We advise on all aspects of claim procedures as well as claim preparation and enforcement (or defence) strategies; <span class="more-mark"></span></p>
  </div>
  <div class="practice-item" style="top:348px">
    <h3>Commercial Litigation</h3>
    <p>We have a reputation for producing excellent results for our litigation clients. Since 1996, the firm has an excellent track record in winning for our clients in commercial disputes. The Firm has built effective litigation machinery that actively involves all advocates; this machinery ensures formulation of accurate legal strategies and efficient modes of execution. <span class="more-mark"></span></p>
  </div>
  <div class="practice-item" style="top:558px">
    <h3>Arbitration</h3>
    <p>We advise clients on both domestic and international arbitration proceedings and other forms of intermediate and alternative dispute resolution, as well as on contract management of claims arising during the course of a project. <span class="more-mark"></span></p>
  </div>
  <div class="btn-light">Read More</div>
</section>

<section class="professionals">
  <h2 class="section-title" style="left:0;width:1200px;text-align:center;top:68px"><em>Our</em> Professionals</h2>
  <div class="rule" style="left:91px;top:118px;width:1018px;background:#c9c9c9"></div>
  <svg class="carousel-arrow" style="left:56px" width="26" height="44" viewBox="0 0 26 44"><path d="M22 4 4 22l18 18" stroke="#999" stroke-width="4" fill="none"/></svg>
  <svg class="carousel-arrow" style="left:1114px" width="26" height="44" viewBox="0 0 26 44"><path d="M4 4l18 18L4 40" stroke="#999" stroke-width="4" fill="none"/></svg>

  <article class="team-card" style="left:135px">
    <div class="team-photo" role="img" aria-label="Portrait photograph of the managing partner"></div>
    <div class="team-body">
      <h4>JABARI.K.TEMBO</h4><div class="role">Managing Partner</div>
      <p>Jabari Kato Tembo is currently the Managing Partner of the firm. He has over 28 years' experience having acted for Central Reserve Bank, Meridian Bank Limited, Petrova Energy Limited among other notable organizations. Jabari is also highly experienced as a transactional lawyer</p>
      <svg class="go" width="18" height="10" viewBox="0 0 18 10"><path d="M0 5h16M12 1l4 4-4 4" stroke="#fff" stroke-width="1.5" fill="none"/></svg>
    </div>
  </article>
  <article class="team-card" style="left:458px">
    <div class="team-photo" role="img" aria-label="Portrait photograph of the senior partner"></div>
    <div class="team-body">
      <h4>DANIEL.S.LUSANI</h4><div class="role">Senior Partner</div>
      <p>Daniel is a Senior Partner at the Firm with over 32 years' experience in Construction law, arbitration and commercial litigation. Daniel is an expert in the Harbor Suite of contracts published by the Global Council of Project Engineers, the Arden Engineering and Construction</p>
      <svg class="go" width="18" height="10" viewBox="0 0 18 10"><path d="M0 5h16M12 1l4 4-4 4" stroke="#fff" stroke-width="1.5" fill="none"/></svg>
    </div>
  </article>
  <article class="team-card" style="left:781px">
    <div class="team-photo" role="img" aria-label="Portrait photograph of the head of litigation"></div>
    <div class="team-body">
      <h4>SIMON OKELLO</h4><div class="role">Partner (Head of Litigation)</div>
      <p>Simon is a Partner at the Firm heading the Litigation Department. Simon started out his career in 2011 with Mirembe Nsubuga &amp; Co. Advocates as a Legal Assistant. He joined the firm in 2014 as an Associate becoming a Senior Associate in 2016 and Partner in 2018.</p>
      <svg class="go" width="18" height="10" viewBox="0 0 18 10"><path d="M0 5h16M12 1l4 4-4 4" stroke="#fff" stroke-width="1.5" fill="none"/></svg>
    </div>
  </article>
</section>

<h2 class="section-title" style="left:0;width:1200px;text-align:center;top:3167px"><em>Our</em> Clients</h2>
<div class="rule" style="left:91px;top:3217px;width:1018px"></div>
<div class="client-row">
  <div class="client"><span>Swiftline</span></div>
  <div class="client"><span>Savanna Foods</span></div>
  <div class="client"><span>Redcrest</span></div>
  <div class="client"><span>Unity Assure</span></div>
  <div class="client"><span>Boxwell</span></div>
  <div class="client"><span>Bluewave</span></div>
  <div class="client"><span>Greenfield</span></div>
</div>
<div class="btn-outline" style="left:526px;top:3438px">Read More</div>

<footer class="site-footer">
  <div class="footer-column-photo" role="img" aria-label="Photograph of classical stone columns"></div>
  <div class="footer-brand"><i></i>Tembo &amp; Lusani</div>
  <div class="footer-heading" style="left:136px;top:160px">QUICK LINKS</div>
  <div class="footer-rule" style="left:136px;top:186px;width:150px"></div>
  <ul class="quick-links">
    <li>About Us</li><li>Practice Areas</li><li>Our clients</li><li>Our Professionals</li><li>Contact Us</li>
  </ul>
  <div class="footer-heading" style="left:397px;top:160px">CONTACT</div>
  <div class="footer-rule" style="left:397px;top:186px;width:150px"></div>
  <div class="contact-block">
    Head Office Address &amp; Contacts<br>Plot 14, Acacia Road<br>3rd Floor, Suite House<br>P. O. Box 6624,<br>Kampala, Uganda.<br><br>
    <div class="contact-line"><i></i>0414 555 210</div>
    <div class="contact-line"><i></i>+256 (0) 700 555 318</div>
    <div class="contact-line"><i></i>info@tembolusani.com</div>
    <div class="contact-line"><i></i>www.tembolusani.com</div>
  </div>
  <div class="footer-heading" style="left:136px;top:400px">FOLLOW US ON</div>
  <div class="footer-rule" style="left:136px;top:426px;width:200px"></div>
  <div class="socials footer-socials"><span></span><span></span><span></span><span></span><span></span></div>
  <div class="footer-heading" style="left:397px;top:400px">CALL US ON</div>
  <div class="footer-rule" style="left:397px;top:426px;width:200px"></div>
  <div class="footer-phone">0414 555 210</div>
  <div class="copyright">© 2017 Tembo &amp; Lusani &nbsp;|&nbsp; Privacy Policy &nbsp;|&nbsp; User Agreement</div>
</footer>

</body>
</html>
```